"Hope and Harbour by Mae" Web Site

I would like a web site designed for my funeral and wedding celebrancy business. My logo was designed by Pixel Quarry (attached). I have written content of the web pages for reference (attached). I have attached logos designed through pixel quarry and photos.
I am sure what else to write in a project description and would welcome suggestions

Target Market(s)

for marriages - brides and grooms, for funerals - families who have lost a loved one

Industry/Entity Type

Wedding Planner

Number of Pages Required

4 page

Font styles to use
Sans Serif

Colors
886aae
3277b5
33a6d7
a64599
e34096

Requirements
Must have
• a call to action (contact me) throughout
Nice to have
• nil
Should not have
• no morbid images

```html
<!DOCTYPE html>
<html lang="en">
<head>
<meta charset="utf-8">
<title>Hope and Harbour by Mae — Marriages</title>
<link href="https://fonts.googleapis.com/css2?family=Great+Vibes&family=Allura&family=Cinzel:wght@700&display=swap" rel="stylesheet">
<style>
  :root {
    --purple: #886aae;
    --deep-purple: #6b4f93;
    --blue: #33a6d7;
    --dark-blue: #3277b5;
    --plum: #a64599;
    --pink: #e34096;
    --white: #ffffff;
    --ink: #3a3a3a;
  }
  * { box-sizing: border-box; margin: 0; padding: 0; }
  html, body { width: 1200px; height: 4206px; overflow: hidden; background: var(--white); }
  body { position: relative; font-family: "Allura", cursive; color: var(--white); }
  .abs { position: absolute; }

  /* header */
  .site-header { position: absolute; left: 0; top: 0; width: 1200px; height: 185px; background: var(--white); }
  .brand { position: absolute; left: 0; width: 1200px; top: 20px; text-align: center; }
  .brand-mark { width: 96px; height: 96px; border-radius: 50%; background: var(--purple); margin: 0 auto 10px; }
  .brand-name { font-family: "Cinzel", serif; font-weight: 700; font-size: 38px; color: var(--deep-purple); letter-spacing: 1px; }

  .main-nav { position: absolute; left: 0; top: 185px; width: 1200px; height: 62px; background: var(--purple); display: flex; }
  .main-nav a { flex: 1; text-align: center; line-height: 62px; font-family: "Great Vibes", cursive; font-size: 36px; color: var(--white); text-decoration: none; }
  .main-nav a.is-active { background: var(--blue); }

  /* hero */
  .hero { position: absolute; left: 0; top: 247px; width: 1200px; height: 722px;
    background: linear-gradient(120deg, #c9a98a 0%, #8a6a52 35%, #3d2c24 70%, #1e1a1c 100%); }
  .hero-title { position: absolute; left: 0; width: 1200px; top: 540px; text-align: center; font-family: "Great Vibes", cursive; font-size: 84px; color: var(--white); }
  .call-button { position: absolute; left: 390px; top: 650px; width: 422px; height: 50px; background: var(--pink); color: var(--white);
    display: flex; align-items: center; justify-content: center; gap: 18px; font-family: "Great Vibes", cursive; font-size: 40px; }
  .rule { position: absolute; left: 0; width: 1200px; height: 6px; background: var(--purple); }

  /* services */
  .services { position: absolute; left: 0; top: 975px; width: 1200px; height: 745px; background: var(--blue); }
  .service { position: absolute; top: 68px; width: 270px; text-align: center; }
  .service-photo { width: 252px; height: 252px; margin: 0 auto; border-radius: 50%; border: 8px solid var(--white);
    background: radial-gradient(circle at 50% 40%, #c9d9b4 0%, #7f9b66 60%, #4d6a3e 100%); }
  .service h3 { font-family: "Great Vibes", cursive; font-weight: 400; font-size: 42px; margin-top: 38px; }
  .service p { font-size: 22px; line-height: 1.28; margin-top: 22px; }

  /* about */
  .about-frame { position: absolute; left: 46px; top: 1880px; width: 642px; height: 430px; border: 16px solid var(--pink); }
  .about-photo { position: absolute; left: 98px; top: 1840px; width: 628px; height: 416px;
    background: linear-gradient(160deg, #f1f0ef 0%, #d8d4d0 45%, #9f8a7a 100%); }
  .about-text { position: absolute; left: 770px; top: 1838px; width: 400px; font-size: 26px; line-height: 1.25; color: var(--blue); }

  /* details */
  .details { position: absolute; left: 0; top: 2442px; width: 1200px; height: 995px; background: var(--blue); }
  .details-frame { position: absolute; left: 822px; top: 78px; width: 240px; height: 272px; border: 14px solid var(--pink); }
  .details-photo { position: absolute; left: 790px; top: 52px; width: 232px; height: 260px; border: 4px solid var(--white);
    background: linear-gradient(170deg, #e9e3df 0%, #c7a79a 55%, #6b6e74 100%); }
  .details-intro { position: absolute; left: 52px; top: 110px; font-size: 26px; }
  .offer-list { position: absolute; left: 52px; top: 150px; list-style: none; font-size: 26px; line-height: 1.28; }
  .offer-list li { padding-left: 44px; position: relative; }
  .offer-list li::before { content: ""; position: absolute; left: 0; top: 9px; width: 14px; height: 14px; border-radius: 50%; background: var(--white); }
  .legal { position: absolute; left: 52px; top: 440px; width: 1100px; font-size: 24px; line-height: 1.3; }
  .legal p + p { margin-top: 24px; }

  /* contact */
  .contact { position: absolute; left: 0; top: 3442px; width: 1200px; height: 708px;
    background: linear-gradient(180deg, #4a4a5c 0%, #6b6170 45%, #8a7a70 75%, #6e5e52 100%); }
  .contact h2 { position: absolute; left: 0; width: 1200px; top: 30px; text-align: center; font-family: "Great Vibes", cursive; font-weight: 400; font-size: 86px; }
  .field { position: absolute; height: 56px; background: rgba(51,166,215,0.82); font-size: 24px; padding: 8px 14px; }
  .field.message { height: 120px; }
  .send-button { position: absolute; left: 45px; top: 482px; width: 260px; height: 56px; background: var(--purple);
    font-family: "Great Vibes", cursive; font-size: 38px; text-align: center; line-height: 56px; }
  .contact-item { position: absolute; left: 712px; display: flex; gap: 22px; align-items: flex-start; font-family: "Great Vibes", cursive; font-size: 42px; line-height: 1.15; }
  .contact-item svg { flex: none; margin-top: 6px; }

  .site-footer { position: absolute; left: 0; top: 4150px; width: 1200px; height: 56px; background: var(--purple);
    text-align: center; line-height: 56px; font-size: 26px; }
</style>
</head>
<body>

<header class="site-header">
  <div class="brand">
    <div class="brand-mark"></div>
    <div class="brand-name">Hope and Harbour by Mae</div>
  </div>
</header>

<nav class="main-nav">
  <a href="#">Home</a>
  <a href="#">About</a>
  <a href="#" class="is-active">Services ∨</a>
  <a href="#">Contact</a>
</nav>

<section class="hero" role="img" aria-label="Bride and groom holding hands as the wedding ring is placed, with a bouquet of roses">
  <h1 class="hero-title">Marriages</h1>
  <div class="call-button">
    <svg width="30" height="30" viewBox="0 0 24 24" aria-hidden="true"><path fill="#fff" d="M6.6 10.8c1.4 2.8 3.8 5.1 6.6 6.6l2.2-2.2c.3-.3.7-.4 1-.2 1.1.4 2.3.6 3.6.6.6 0 1 .4 1 1V20c0 .6-.4 1-1 1C10.6 21 3 13.4 3 4c0-.6.4-1 1-1h3.5c.6 0 1 .4 1 1 0 1.3.2 2.5.6 3.6.1.3 0 .7-.2 1l-2.3 2.2z"/></svg>
    <span>(+61) 0400 271 635</span>
  </div>
</section>

<div class="rule" style="top:969px"></div>

<section class="services">
  <article class="service" style="left:39px">
    <div class="service-photo" role="img" aria-label="Celebrant with a bride on a garden veranda"></div>
    <h3>Title Here</h3>
    <p>Lorem ipsum dolor sit amet, consectetuer adipiscing elit, sed diam nonummy nibh euismod tincidunt ut laoreet dolore magna aliquam erat volutpat. Ut wisi enim ad minim veniam, quis nostrud exerci tation ullamcorper suscipit lobortis nisl ut aliquip ex ea commodo consequat. Duis autem vel eum iriure dolor in hendrerit in vulputate velit esse molestie consequat, vel illum dolore eu feugiat nulla facilisis at vero eros et</p>
  </article>
  <article class="service" style="left:319px">
    <div class="service-photo" role="img" aria-label="Celebrant with a bride on a garden veranda"></div>
    <h3>Title Here</h3>
    <p>Lorem ipsum dolor sit amet, consectetuer adipiscing elit, sed diam nonummy nibh euismod tincidunt ut laoreet dolore magna aliquam erat volutpat. Ut wisi enim ad minim veniam, quis nostrud exerci tation ullamcorper suscipit lobortis nisl ut aliquip ex ea commodo consequat. Duis autem vel eum iriure dolor in hendrerit in vulputate velit esse molestie consequat, vel illum dolore eu feugiat nulla facilisis at vero eros et</p>
  </article>
  <article class="service" style="left:599px">
    <div class="service-photo" role="img" aria-label="Celebrant with a bride on a garden veranda"></div>
    <h3>Title Here</h3>
    <p>Lorem ipsum dolor sit amet, consectetuer adipiscing elit, sed diam nonummy nibh euismod tincidunt ut laoreet dolore magna aliquam erat volutpat. Ut wisi enim ad minim veniam, quis nostrud exerci tation ullamcorper suscipit lobortis nisl ut aliquip ex ea commodo consequat. Duis autem vel eum iriure dolor in hendrerit in vulputate velit esse molestie consequat, vel illum dolore eu feugiat nulla facilisis at vero eros et</p>
  </article>
  <article class="service" style="left:887px">
    <div class="service-photo" role="img" aria-label="Celebrant with a bride on a garden veranda"></div>
    <h3>Title Here</h3>
    <p>Lorem ipsum dolor sit amet, consectetuer adipiscing elit, sed diam nonummy nibh euismod tincidunt ut laoreet dolore magna aliquam erat volutpat. Ut wisi enim ad minim veniam, quis nostrud exerci tation ullamcorper suscipit lobortis nisl ut aliquip ex ea commodo consequat. Duis autem vel eum iriure dolor in hendrerit in vulputate velit esse molestie consequat, vel illum dolore eu feugiat nulla facilisis at vero eros et</p>
  </article>
</section>

<div class="rule" style="top:1714px;height:4px"></div>

<div class="about-frame"></div>
<div class="about-photo" role="img" aria-label="Celebrant speaking into a microphone in front of white curtains"></div>
<p class="about-text">Your wedding day is one of the most significant and happy days of your life. Accordingly, you need to choose people and suppliers who can deliver on your wishes and desires for your special day. As your Celebrant, I will work with you both to design and deliver a ceremony that authentically reflects your love and life together and tells your story. From a traditional wedding ceremony to a funky, themed ceremony, I am willing to assist you in any location, at any time, to make it your special day. I am located in Perth and Marlow Bay in the South of Western Australia, but I am happy to travel for your special day.</p>

<div class="rule" style="top:2436px"></div>

<section class="details">
  <div class="details-frame"></div>
  <div class="details-photo" role="img" aria-label="Celebrant in a pink jacket speaking at a lectern"></div>
  <p class="details-intro">Through Hope and Harbour by Mae, I will provide a range of services for your marriage, including:</p>
  <ul class="offer-list">
    <li>Initial meeting and unlimited follow-up contact to answer all your questions,</li>
    <li>All the legalities</li>
    <li>Design of your ceremony with you including sample services, ideas, vows, etc.</li>
    <li>A rehearsal of your ceremony.</li>
    <li>Design and delivery of an authentic ceremony that truly reflects you as a couple.</li>
    <li>A copy of your ceremony.</li>
    <li>PA system</li>
    <li>Signing table and chairs (if needed)</li>
  </ul>
  <div class="legal">
    <p>The Legal Stuff:<br>I am legally authorised by the Commonwealth Attorney General's department to perform marriages across Australia. Whether it's me or someone else you chose to work with you on your marriage, ensure that they are equipped to do so. A good celebrant will not only walk you through the legalities of marriage, and also create a ceremony which truly reflects your authentic partnership.</p>
    <p>I will assist you to understand the legal requirements of marriage and also the notice of intended marriage which must be given to me at least one month, and up to 18 months, before your wedding. I will need to see your evidence of date and place of birth, identity and evidence of the end of any previous marriage for you or your partner. If there is less than a month before your wedding, a prescribed authority may approve a shorter notice in some limited circumstances.</p>
    <p>On the day of your wedding, we will sign 3 marriage certificates along with 2 witnesses. I will then register your marriage with the Registry of births, deaths and marriages in the state or territory in which I marry you.</p>
    <p>As an authorised Celebrant, I charge a range of fees for my services, depending on the type and location of your wedding. I also require a non-refundable deposit once you have agreed to use my celebrancy services. Please contact me and we can discuss your needs and my fees.</p>
  </div>
</section>

<div class="rule" style="top:3436px"></div>

<section class="contact" role="img" aria-label="Celebrant on a beach at dusk with arms outstretched beside a white draped wedding arch">
  <h2>Contact Me</h2>
  <div class="field" style="left:45px;top:130px;width:258px">Name:</div>
  <div class="field" style="left:322px;top:130px;width:266px">Email:</div>
  <div class="field" style="left:45px;top:270px;width:258px">Address:</div>
  <div class="field" style="left:322px;top:270px;width:266px">Contact #:</div>
  <div class="field message" style="left:45px;top:340px;width:543px">Message:</div>
  <div class="send-button">Send</div>

  <div class="contact-item" style="top:160px">
    <svg width="34" height="34" viewBox="0 0 24 24" aria-hidden="true"><path fill="#33a6d7" d="M12 3 2 12h3v9h5v-6h4v6h5v-9h3z"/></svg>
    <div>Mae Harlow<br>PO Box 812, Larkfield<br>6031, Western Australia</div>
  </div>
  <div class="contact-item" style="top:405px">
    <svg width="30" height="30" viewBox="0 0 24 24" aria-hidden="true"><path fill="#33a6d7" d="M6.6 10.8c1.4 2.8 3.8 5.1 6.6 6.6l2.2-2.2c.3-.3.7-.4 1-.2 1.1.4 2.3.6 3.6.6.6 0 1 .4 1 1V20c0 .6-.4 1-1 1C10.6 21 3 13.4 3 4c0-.6.4-1 1-1h3.5c.6 0 1 .4 1 1 0 1.3.2 2.5.6 3.6.1.3 0 .7-.2 1l-2.3 2.2z"/></svg>
    <div>Phone: (+61) 0400 271 635</div>
  </div>
  <div class="contact-item" style="top:500px">
    <svg width="34" height="30" viewBox="0 0 24 20" aria-hidden="true"><rect x="1" y="2" width="22" height="16" fill="#33a6d7"/><path d="M1 3l11 8 11-8" fill="none" stroke="#fff" stroke-width="1.6"/></svg>
    <div>Email: mae@hopeharbour.example</div>
  </div>
</section>

<footer class="site-footer">Copyright 2018 | Hope and Harbour by Mae</footer>

</body>
</html>
```